Report presentation for measurement or inline reports

First page of report. Our inline reporting will come in a maintenance map. We want a modern first page and a real eye-catcher for a new company based in the Netherlands called: RTP Luchtregeling B.V. We are a service company witch measures, balances and give advices at indoor climate HVAC installations. We would like to see designs that use the color blue. We deliver our services to different buildings: Hospitals, atractions, officebuildings, government buildings, swimming pools and schools. Our website: www.rtpl.nl
Updates

Can you all add the new logo please. The companyname is RTP Luchtregeling B.V.. In witch format can i retrieve the design?

Industry/Entity Type

It Company

Colors
0255a3
3176b5
85abd2
cedeed
eaf1f7
ffffff

Requirements
Must have
• Projectname; projectplace; Inline or measure report; date; logo; companyname. it must be easy printable so not to much colours.
• The companyname is: RTP Luchtregeling B.V.. Please add the name. A new logo is updated.
Nice to have
• Maybe some pictures from hvac installations, buildings or measure

```html
<!DOCTYPE html>
<html lang="nl">
<head>
<meta charset="utf-8">
<title>Inline Report – RTP Luchtregeling B.V.</title>
<link rel="stylesheet" href="https://fonts.googleapis.com/css2?family=Roboto:wght@400;500;700&display=swap">
<style>
  :root {
    --page-bg: #f3f3f3;
    --paper: #f7f9fa;
    --brand-navy: #0b5184;
    --panel-blue: #b7cde4;
    --text-grey: #5a5f66;
    --white: #ffffff;
    --photo-light: #c9d6e2;
    --photo-mid: #9fb1c2;
    --photo-dark: #4a5560;
  }
  html, body {
    margin: 0;
    width: 1200px;
    height: 1000px;
    overflow: hidden;
    background: var(--page-bg);
    font-family: "Roboto", Arial, sans-serif;
  }
  .report-cover {
    position: absolute;
    left: 245px;
    top: 41px;
    width: 645px;
    height: 835px;
    transform: scale(1.1);
    transform-origin: 0 0;
    background: var(--paper);
    overflow: hidden;
  }
  .cover-art {
    position: absolute;
    inset: 0;
    width: 645px;
    height: 835px;
  }
  .report-type {
    position: absolute;
    left: 174px;
    top: 158px;
    margin: 0;
    font-size: 24px;
    font-weight: 500;
    color: var(--white);
    letter-spacing: 0.2px;
  }
  .project-name {
    position: absolute;
    left: 174px;
    top: 186px;
    margin: 0;
    font-size: 52px;
    font-weight: 700;
    line-height: 1;
    color: var(--brand-navy);
    letter-spacing: -0.5px;
  }
  .project-place {
    position: absolute;
    right: 90px;
    top: 240px;
    margin: 0;
    font-size: 18px;
    color: var(--text-grey);
  }
  .report-date {
    position: absolute;
    right: 92px;
    top: 318px;
    margin: 0;
    font-size: 35px;
    font-weight: 700;
    color: var(--brand-navy);
  }
  .company-name {
    position: absolute;
    right: 94px;
    top: 358px;
    margin: 0;
    font-size: 18px;
    color: var(--text-grey);
  }
  .brand-mark {
    position: absolute;
    left: 35px;
    top: 818px;
    width: 343px;
    height: 66px;
    transform: rotate(-90deg);
    transform-origin: 0 0;
    display: flex;
    align-items: center;
    gap: 10px;
    padding-left: 14px;
    box-sizing: border-box;
  }
  .brand-square {
    width: 22px;
    height: 22px;
    background: var(--brand-navy);
    flex: none;
  }
  .brand-name {
    font-size: 22px;
    font-weight: 700;
    color: var(--brand-navy);
    white-space: nowrap;
  }
</style>
</head>
<body>
  <main class="report-cover">
    <svg class="cover-art" viewBox="0 0 645 835" xmlns="http://www.w3.org/2000/svg">
      <defs>
        <linearGradient id="buildingTones" x1="0" y1="0" x2="1" y2="1">
          <stop offset="0" stop-color="var(--photo-mid)"/>
          <stop offset="0.55" stop-color="var(--photo-light)"/>
          <stop offset="1" stop-color="var(--photo-dark)"/>
        </linearGradient>
      </defs>
      <g role="img" aria-label="Photo of a modern glass office building facade seen from below">
        <polygon class="building-photo" points="0,520 300,255 475,470 645,308 645,835 0,835" fill="url(#buildingTones)"/>
      </g>
      <polygon class="accent-bar" points="35,0 101,0 101,408 35,465" fill="var(--brand-navy)"/>
      <rect class="title-panel" x="134" y="100" width="363" height="735" fill="var(--panel-blue)" opacity="0.88"/>
      <rect class="veil-box" x="292" y="482" width="265" height="353" fill="var(--white)" opacity="0.45"/>
      <polygon class="logo-strip" points="35,530 101,475 101,818 35,818" fill="var(--white)"/>
    </svg>

    <p class="report-type">INLINE REPORT</p>
    <h1 class="project-name">PROJECT NAME</h1>
    <p class="project-place">PROJECT PLACE</p>
    <p class="report-date">5/2/2018</p>
    <p class="company-name">RTP Luchtregeling B.V.</p>

    <div class="brand-mark">
      <span class="brand-square"></span>
      <span class="brand-name">RTP Luchtregeling</span>
    </div>
  </main>
</body>
</html>
```